Brolvane Co.,Ltd. need business card

Brolvane Company Limited is a facility management company. We provides a total solution services from administration, energy saving, security, safety, food catering to companies.

The logo should be in elegant style with innovative that suited to the upper market
Please see the logo image in the attached file. You can use this Red or Blue or Green checkerboard (color and font should be similar to logo) as the main part of business card (can be an entire of one side of business card) . In another side of card should contain contact details of personnel - here below demo information

Kanyarat Thoengsai
Chief Executive Officer

No.73, Soi 5, Ruam Wongsa Road
Nong Khaem, Bangkok,
10520, Thailand

Tel + 66841537296
Mobile + 66841537296
E-mail: Kanyarat.Thoengsai@brolvane-example.co.th

Target Market(s)

Factory, Hotel and Hospital

Industry/Entity Type

Business

Contact Information for Business Card

Kanyarat Thoengsai
Chief Executive Officer

Nong Khaem, Bangkok,
10520, Thailand

Tel + 66841537296
Mobile + 66841537296

We will change details with the winner designer

Font styles to use
Sans Serif

Requirements
Must have
• In style of red checkerboard and white color

```html
<!DOCTYPE html>
<html lang="en">
<head>
<meta charset="utf-8">
<title>Brolvane Co.,Ltd. — Business Card</title>
<link rel="stylesheet" href="https://fonts.googleapis.com/css2?family=Libre+Baskerville:wght@400;700&display=swap">
<style>
  :root {
    --backdrop: #ece8e3;
    --card-red: #b2303e;
    --card-red-deep: #a62a37;
    --ink-white: #ffffff;
    --shadow: rgba(60, 30, 30, 0.22);
  }
  * { box-sizing: border-box; margin: 0; padding: 0; }
  html, body { width: 1200px; height: 800px; overflow: hidden; }
  body {
    background: var(--backdrop);
    font-family: "Libre Baskerville", Georgia, serif;
    color: var(--ink-white);
    display: flex;
    align-items: center;
    justify-content: center;
    gap: 50px;
  }
  .card {
    position: relative;
    width: 520px;
    height: 298px;
    background: var(--card-red);
    box-shadow: 0 10px 26px var(--shadow);
    overflow: hidden;
  }
  .card-pattern {
    position: absolute;
    inset: 0;
    background: linear-gradient(135deg, var(--card-red) 0%, var(--card-red-deep) 100%);
  }
  .brand-name {
    position: relative;
    font-weight: 400;
    text-transform: uppercase;
    letter-spacing: 0.32em;
    color: var(--ink-white);
  }
  /* Contact side */
  .card-contact .brand-name {
    position: absolute;
    top: 30px;
    left: 34px;
    font-size: 40px;
  }
  .person {
    position: absolute;
    top: 118px;
    left: 34px;
    width: 230px;
  }
  .person-name {
    font-size: 15px;
    font-weight: 700;
    letter-spacing: 0.01em;
  }
  .person-title {
    font-size: 11px;
    margin-top: 3px;
  }
  .rule {
    border: none;
    border-top: 1px solid var(--ink-white);
    margin: 8px 0 10px;
  }
  .contact-list {
    list-style: none;
    font-size: 10.5px;
    line-height: 1.6;
  }
  .address {
    position: absolute;
    right: 30px;
    bottom: 26px;
    width: 230px;
    font-style: normal;
    text-align: right;
    font-size: 11px;
    line-height: 1.6;
  }
  .address .rule { margin: 0 0 8px; }
  /* Brand side */
  .card-brand {
    display: flex;
    align-items: center;
    justify-content: center;
  }
  .card-brand .brand-name {
    font-size: 46px;
    letter-spacing: 0.3em;
    margin-right: -0.3em;
  }
</style>
</head>
<body>
  <section class="card card-contact" aria-label="Business card, contact side">
    <div class="card-pattern" role="img" aria-label="Red checkerboard pattern background"></div>
    <p class="brand-name">Brolvane</p>
    <div class="person">
      <p class="person-name">Kanyarat Thoengsai</p>
      <p class="person-title">Chief Executive Officer</p>
      <hr class="rule">
      <ul class="contact-list">
        <li>Tel + 66841537296</li>
        <li>Mobile + 66841537296</li>
        <li>E-mail: Kanyarat.Thoengsai@brolvane-example.co.th</li>
      </ul>
    </div>
    <address class="address">
      <hr class="rule">
      No.73, Soi 5, Ruam Wongsa Road<br>
      Nong Khaem, Bangkok<br>
      10520, Thailand
    </address>
  </section>

  <section class="card card-brand" aria-label="Business card, brand side">
    <div class="card-pattern" role="img" aria-label="Red checkerboard pattern background"></div>
    <p class="brand-name">Brolvane</p>
  </section>
</body>
</html>
```